Banner AD

Hi,
I need a banner ad for an email campaign which will act as a link back to my website.
Horizontal Banner - Specs: 1.5” high x 11.5” wide, 72 dpi
Needs to have the following information;
Image - See attached
Logo - See attached
Text - "For connoisseurs of unique, hand crafted, vintage, pin-up and burlesque inspired lingerie and corsets, delectable handmade lotions & potions and naughty & nice, seduce me please gifts and ideas"
www.velvetmorrow.com
Overall look and feel should be in line with website.
Target Market(s)
Women interested in rockabilly, pinup, burlesque, vintage fashion - Ages 25-40
Look and feel
Each slider illustrates characteristics of the customer's brand and the style your logo design should communicate.

```html
<!DOCTYPE html>
<html lang="en">
<head>
<meta charset="utf-8">
<title>Velvet Morrow – Banner</title>
<link href="https://fonts.googleapis.com/css2?family=Archivo+Narrow:wght@400;700&display=swap" rel="stylesheet">
<style>
  :root {
    --ink-black: #080808;
    --damask-grey: #2e2e2e;
    --damask-mid: #1a1a1a;
    --text-white: #ffffff;
    --brand-red: #a8321f;
    --skin-light: #dccdca;
    --skin-mid: #b99c9a;
    --rose-shadow: #5e3a3c;
  }
  html, body {
    margin: 0;
    padding: 0;
    overflow: hidden;
    width: 1200px;
    height: 157px;
    background: var(--ink-black);
  }
  .banner {
    position: relative;
    width: 1200px;
    height: 157px;
    overflow: hidden;
    background: var(--ink-black);
    font-family: "Archivo Narrow", "Arial Narrow", sans-serif;
  }
  .banner__damask {
    position: absolute;
    left: 0;
    top: 0;
    width: 560px;
    height: 157px;
    background:
      radial-gradient(ellipse 260px 120px at 150px 40px, var(--damask-grey) 0%, transparent 70%),
      radial-gradient(ellipse 240px 110px at 400px 120px, var(--damask-grey) 0%, transparent 70%),
      linear-gradient(90deg, var(--damask-mid) 0%, #242424 50%, var(--ink-black) 100%);
  }
  .banner__tagline {
    position: absolute;
    left: 8px;
    top: 13px;
    width: 500px;
    margin: 0;
    color: var(--text-white);
    font-weight: 700;
    font-size: 22px;
    line-height: 24.5px;
    text-align: center;
    letter-spacing: -0.1px;
  }
  .banner__photo {
    position: absolute;
    left: 490px;
    top: 0;
    width: 490px;
    height: 157px;
    background:
      radial-gradient(ellipse 200px 140px at 310px 80px, var(--skin-light) 0%, transparent 75%),
      linear-gradient(90deg,
        var(--ink-black) 0%,
        var(--rose-shadow) 15%,
        var(--skin-mid) 32%,
        var(--skin-light) 55%,
        var(--skin-mid) 80%,
        var(--ink-black) 100%);
  }
  .banner__brand {
    position: absolute;
    left: 980px;
    top: 0;
    width: 220px;
    height: 157px;
    text-align: center;
  }
  .banner__mark {
    position: absolute;
    left: 78px;
    top: 22px;
    width: 64px;
    height: 64px;
    border-radius: 50%;
    background: var(--brand-red);
  }
  .banner__name {
    position: absolute;
    left: 0;
    top: 98px;
    width: 220px;
    margin: 0;
    color: var(--brand-red);
    font-weight: 400;
    font-size: 18px;
    letter-spacing: 0.5px;
    text-transform: uppercase;
  }
  .banner__url {
    position: absolute;
    left: 0;
    top: 126px;
    width: 220px;
    color: var(--text-white);
    font-weight: 700;
    font-size: 19px;
    text-decoration: none;
  }
</style>
</head>
<body>
  <div class="banner">
    <div class="banner__damask" role="img" aria-label="Black and charcoal damask wallpaper pattern"></div>
    <p class="banner__tagline">For connoisseurs of unique, hand crafted, vintage,<br>pin-up and burlesque inspired lingerie and corsets,<br>delectable handmade lotions &amp; potions and naughty<br>&amp; nice, seduce me please gifts and ideas</p>
    <div class="banner__photo" role="img" aria-label="Photograph of a pin-up model with dark hair and red lips posing against a pale backdrop"></div>
    <div class="banner__brand">
      <span class="banner__mark" aria-hidden="true"></span>
      <p class="banner__name">Velvet Morrow</p>
      <a class="banner__url" href="#">www.velvetmorrow.com</a>
    </div>
  </div>
</body>
</html>
```